Web design for community centre - bright colours (provided) and matching existing logo

Website based on a provided logo and existing website template skeleton (it is a Wordpress theme we must use that is already installed)

Basically, see if you can improve the existing theme skeleton at https://tarvolnh.org.au/redesign/. Mostly we are looking for a much nicer menu that works with the logo, and a nice font/design for text content.

We have a developer who will work your design into the Wordpress theme – so you can get creative in a graphic software app and our developer can most likely implement your ideas.

The website ideally will include design ideas from the logo (e.g. the idea of people with their arms around each other, colours).

Improvement to the text displayed on the photo slider (e.g. a colour border or other decoration) is also needed.

It needs a 'community' feel.

Target Market(s)

Parents (provides childcare), older people, people with disabilities, recent migrants

Industry/Entity Type

Community Center

Number of Pages Required

1 page

Font styles to use
Sans Serif

Colors

Designer to choose colors to be used in the design.

Requirements
Must have
• A very aesthetic top menu. Nice use of spacing, negative space etc.
• Fonts need to be legally available without a pageview fee (one off purchase OK). You need to provide proof we can use the font legally.
• See https://www.pelmoray.org.au/ for an example of a menu we like.
• Must use the existing logo, provided in this brief.
• Needs to use colours from the logo but do not need to use all of them!
• Must be workable into the theme already installed at https://tarvolnh.org.au/redesign
Nice to have
• Maybe some kind of shapes attached to each menu link (top menu0
• A use of all 5 colours on the top menu, when you hover on it
Should not have
• Serif fonts

```html
<!DOCTYPE html>
<html lang="en">
<head>
<meta charset="utf-8">
<title>Tarvol Neighbourhood Learning Centre</title>
<link href="https://fonts.googleapis.com/css2?family=Exo+2:wght@300;600;700&family=Roboto:wght@400;500;700&display=swap" rel="stylesheet">
<style>
:root{
  --green:#8cc63f;--orange:#f7941d;--blue:#16b1e8;--pink:#ec1e79;--purple:#6a3393;
  --ink:#222;--grey:#ececec;--text:#333;
  --fb:#3b5998;--ig:#3f729b;--tw:#55acee;--vm:#5bc2f0;
}
*{box-sizing:border-box;margin:0;padding:0}
html,body{width:853px;height:1200px;overflow:hidden;background:#fff;font-family:"Roboto",sans-serif;color:var(--text)}
.page{position:relative;width:853px;height:1200px}
.abs{position:absolute}
.brand{left:40px;top:14px;display:flex;align-items:center;gap:9px}
.brand-dot{width:66px;height:66px;border-radius:50%;background:var(--green)}
.brand-name{font-family:"Exo 2",sans-serif;font-weight:600;font-size:19.5px;line-height:19.5px;color:var(--ink)}
.divider{left:314px;top:15px;width:1px;height:65px;background:#ddd}
.contact{font-size:9.5px;line-height:15px;color:#444;white-space:nowrap}
.contact svg{position:absolute;left:-16px;top:1px}
.nav{top:98px;left:0;width:853px;height:34px}
.nav a{position:absolute;top:0;height:34px;display:flex;align-items:center;justify-content:center;color:#fff;font-size:9.5px;font-weight:700;letter-spacing:.5px;text-decoration:none}
.band{top:131px;left:0;width:853px;height:355px;background:var(--grey);box-shadow:inset 0 4px 4px -2px rgba(0,0,0,.15)}
.slider{left:40px;top:156px;width:503px;height:300px;background:linear-gradient(135deg,#4a3526,#7b5a41 40%,#c79a7f 60%,#5a3e2c)}
.caption{left:40px;top:220px;width:187px;height:172px;background:rgba(40,28,20,.6);border-right:2px solid var(--blue);padding:22px 12px 0 44px}
.caption h2{font-family:"Exo 2",sans-serif;font-weight:700;font-size:21px;line-height:24px;color:var(--blue);margin-bottom:4px}
.caption p{color:#fff;font-size:9.6px;line-height:16.2px;white-space:nowrap}
.arrow{top:297px}
.sub-title{left:582px;top:201px;font-family:"Exo 2",sans-serif;font-weight:300;font-size:19.5px;line-height:22px;color:var(--ink)}
.sub-title b{font-weight:700}
.field{background:#fff;border:1px solid #d6d6d6;font-size:9px;color:#888;padding-left:7px;display:flex;align-items:center}
.btn{background:var(--orange);color:#fff;font-weight:700;display:flex;align-items:center;justify-content:center}
.social{display:flex;gap:5px}
.social span{width:33px;height:33px;display:block}
.tiles{left:39px;top:541px;width:773px;display:grid;grid-template-columns:repeat(4,193px);grid-auto-rows:170px}
.tile{color:#fff;text-align:center;padding-top:26px}
.tile h3{font-family:"Exo 2",sans-serif;font-weight:300;font-size:22.5px;line-height:26px;margin-bottom:9px}
.tile p{font-size:9.4px;line-height:13.8px;white-space:nowrap;color:rgba(255,255,255,.92)}
.tile a{display:inline-block;margin-top:15px;color:#fff;font-size:8.5px;font-weight:500;letter-spacing:.6px}
.photo{display:block}
.footer{left:0;top:941px;width:853px;height:259px;background:var(--grey)}
.f-head{top:972px;font-family:"Exo 2",sans-serif;font-weight:300;font-size:15.5px;color:var(--ink)}
.rule{left:40px;top:1094px;width:419px;height:1px;background:#ccc}
.copy{left:40px;top:1107px;font-size:8.3px;color:#222}
.grass{left:0;top:1118px;width:853px;height:82px;background:linear-gradient(to bottom,rgba(120,190,50,0),#7cbf2e 45%,#4f9a1e)}
</style>
</head>
<body>
<div class="page">
  <header>
    <div class="abs brand"><span class="brand-dot"></span><div class="brand-name">Tarvol<br>Neighbourhood<br>Learning Centre</div></div>
    <div class="abs divider"></div>
    <div class="abs contact" style="left:364px;top:32px">
      <svg width="10" height="12" viewBox="0 0 10 12"><path d="M5 0a4 4 0 0 0-4 4c0 3 4 8 4 8s4-5 4-8a4 4 0 0 0-4-4z" fill="var(--orange)"/><circle cx="5" cy="4" r="1.5" fill="#fff"/></svg>
      47 Wattle Street<br>Brindabel VC 3184
    </div>
    <div class="abs contact" style="left:512px;top:32px">
      <svg width="10" height="10" viewBox="0 0 10 10"><path d="M2 0l2 2.5-1 1.2a6 6 0 0 0 3.3 3.3l1.2-1L10 8l-1.5 2C4 10 0 6 0 1.5z" fill="var(--orange)"/></svg>
      02 555 018 294<br>
      <span style="position:relative">
        <svg width="10" height="8" viewBox="0 0 10 8" style="left:-16px;top:3px"><rect x=".5" y=".5" width="9" height="7" fill="none" stroke="var(--orange)"/><path d="M.5.5l4.5 4 4.5-4" fill="none" stroke="var(--orange)"/></svg>
        info@tarvolnh.org.au
      </span>
    </div>
  </header>

  <nav class="abs nav">
    <a href="#" style="left:39px;width:57px;background:var(--green)">HOME</a>
    <a href="#" style="left:102px;width:73px;background:var(--orange)">COURSES</a>
    <a href="#" style="left:182px;width:137px;background:var(--blue)">SOCIAL ENTERPRISE</a>
    <a href="#" style="left:325px;width:173px;background:var(--pink)">COMMUNITY PROGRAMS</a>
    <a href="#" style="left:504px;width:85px;background:var(--purple)">TARVOL CARES</a>
    <a href="#" style="left:595px;width:95px;background:var(--green)">VENUE HIRE</a>
    <a href="#" style="left:697px;width:115px;background:var(--orange)">SPARESEAT CAFÉ</a>
  </nav>

  <section class="abs band"></section>
  <div class="abs slider" role="img" aria-label="Photo of several hands placed together on a wooden table"></div>
  <div class="abs caption">
    <h2>Hands</h2>
    <p>Our accredited Childcare<br>and Kinder allows your<br>child to grown in a fun<br>learning environment,<br>while you attend courses<br>or activities</p>
  </div>
  <svg class="abs arrow" style="left:49px" width="12" height="18" viewBox="0 0 12 18"><path d="M10 2L3 9l7 7" fill="none" stroke="rgba(255,255,255,.7)" stroke-width="3"/></svg>
  <svg class="abs arrow" style="left:521px" width="12" height="18" viewBox="0 0 12 18"><path d="M2 2l7 7-7 7" fill="none" stroke="rgba(255,255,255,.7)" stroke-width="3"/></svg>

  <div class="abs sub-title">SUBSCRIBE FOR OUR<br><b>NEWSLETTER</b></div>
  <div class="abs field" style="left:583px;top:267px;width:228px;height:30px">Enter your email ...</div>
  <div class="abs btn" style="left:583px;top:309px;width:86px;height:28px;font-size:11px">SUBSCRIBE</div>
  <div class="abs social" style="left:584px;top:367px"><span style="background:var(--fb)"></span><span style="background:var(--ig)"></span><span style="background:var(--tw)"></span><span style="background:var(--vm)"></span></div>

  <section class="abs tiles">
    <div class="photo" role="img" aria-label="Photo of children drawing at a classroom table" style="background:linear-gradient(135deg,#d9c8b0,#e88a5a 55%,#b9a07f)"></div>
    <div class="tile" style="background:var(--green)"><h3>About Us</h3><p>Lorem ipsum dolor sit amet,<br>consectetur adipiscing elit, sed do<br>eiusmod tempor incididunt ut<br>labore et dolore magna aliqua ...</p><a href="#">READ MORE</a></div>
    <div class="photo" role="img" aria-label="Photo of smiling children hugging" style="background:linear-gradient(135deg,#e8e6e0,#e7c84a 50%,#7fd3a8)"></div>
    <div class="tile" style="background:var(--orange)"><h3>Child Care</h3><p>Lorem ipsum dolor sit amet,<br>consectetur adipiscing elit, sed do<br>eiusmod tempor incididunt ut<br>labore et dolore magna aliqua ...</p><a href="#">READ MORE</a></div>
    <div class="tile" style="background:var(--pink)"><h3>Courses</h3><p>Lorem ipsum dolor sit amet,<br>consectetur adipiscing elit, sed do<br>eiusmod tempor incididunt ut<br>labore et dolore magna aliqua ...</p><a href="#">READ MORE</a></div>
    <div class="photo" role="img" aria-label="Photo of a woman and young girl playing with toy blocks" style="background:linear-gradient(135deg,#efe9e2,#c9b6a6 50%,#9fb7c7)"></div>
    <div class="tile" style="background:var(--purple)"><h3>Community</h3><p>Lorem ipsum dolor sit amet,<br>consectetur adipiscing elit, sed do<br>eiusmod tempor incididunt ut<br>labore et dolore magna aliqua ...</p><a href="#">READ MORE</a></div>
    <div class="photo" role="img" aria-label="Photo of older adults exercising with raised arms in a hall" style="background:linear-gradient(135deg,#b8a98f,#7a5a8f 55%,#5a4a3f)"></div>
  </section>

  <footer>
    <div class="abs footer"></div>
    <div class="abs f-head" style="left:40px">TARVOL NEIGHBOURHOOD</div>
    <div class="abs f-head" style="left:291px">SOCIAL MEDIA</div>
    <div class="abs f-head" style="left:530px">ENQUIRY NOW</div>
    <div class="abs contact" style="left:57px;top:1002px">
      <svg width="10" height="12" viewBox="0 0 10 12"><path d="M5 0a4 4 0 0 0-4 4c0 3 4 8 4 8s4-5 4-8a4 4 0 0 0-4-4z" fill="var(--orange)"/><circle cx="5" cy="4" r="1.5" fill="#fff"/></svg>
      47 Wattle Street<br>Brindabel VC 3184
    </div>
    <div class="abs contact" style="left:57px;top:1046px">
      <svg width="10" height="10" viewBox="0 0 10 10"><path d="M2 0l2 2.5-1 1.2a6 6 0 0 0 3.3 3.3l1.2-1L10 8l-1.5 2C4 10 0 6 0 1.5z" fill="var(--orange)"/></svg>
      02 555 018 294<br>
      <span style="position:relative">
        <svg width="10" height="8" viewBox="0 0 10 8" style="left:-16px;top:3px"><rect x=".5" y=".5" width="9" height="7" fill="none" stroke="var(--orange)"/><path d="M.5.5l4.5 4 4.5-4" fill="none" stroke="var(--orange)"/></svg>
        info@tarvolnh.org.au
      </span>
    </div>
    <div class="abs social" style="left:292px;top:1004px"><span style="background:var(--fb)"></span><span style="background:var(--ig)"></span><span style="background:var(--tw)"></span><span style="background:var(--vm)"></span></div>
    <div class="abs field" style="left:530px;top:1004px;width:136px;height:23px;border:none;font-size:8.5px">Name*</div>
    <div class="abs field" style="left:676px;top:1004px;width:136px;height:23px;border:none;font-size:8.5px">Email*</div>
    <div class="abs field" style="left:530px;top:1037px;width:282px;height:35px;border:none;font-size:8.5px;align-items:flex-start;padding-top:5px">Message*</div>
    <div class="abs btn" style="left:530px;top:1083px;width:57px;height:27px;font-size:9.5px">SEND</div>
    <div class="abs rule"></div>
    <div class="abs copy">COPYRIGHT © 2019 <b>TARVOLNH</b> &nbsp;&nbsp; I &nbsp;&nbsp; ALL RIGHT RESERVED.,</div>
    <div class="abs grass" role="img" aria-label="Decorative strip of green grass along the bottom edge"></div>
  </footer>
</div>
</body>
</html>
```